BRIGHTWATER RV Resort needs a logo and advertising poster

We need an advertising poster for our epic RV Resort located on north end of Tuskin Lake, (Northern Saskatchewan, trees no mountains)
SEASONAL FULL SERVICE SITES with marina and lake access.
Sauna/plunge, disc golf , hiking/quad trails, and pet friendly.
We are after a fun 70,s themed simple poster. Please use brand guide for colours and redo logo to be Brightwater Resort.

Target Market(s)

RV owners looking for permeant sites. No tenting.

Font styles to use
Other font styles liked:
• See brand guide

Requirements
Must have
• Change exisiting branding to BRIGHTWATER RESORT instead of coffee Emphasis Limited sites.... Referral discount. Phone number.
Nice to have
• .
Should not have
• Keep it simple

```html
<!DOCTYPE html>
<html lang="en">
<head>
<meta charset="utf-8">
<title>Brightwater Resort – Poster</title>
<link href="https://fonts.googleapis.com/css2?family=Yellowtail&family=Rubik:wght@500;700;800&family=Roboto+Condensed:wght@400;700&display=swap" rel="stylesheet">
<style>
  :root{
    --backdrop:#7a7866;
    --paper:#f8f5e8;
    --ink:#1f2a2c;
    --orange:#f07d22;
    --green:#3f6b5c;
    --pine:#24443b;
    --cream:#f6eecf;
  }
  *{margin:0;padding:0;box-sizing:border-box}
  html,body{width:1200px;height:2308px;overflow:hidden;background:var(--backdrop)}
  .poster{
    position:absolute;left:100px;top:447px;width:1000px;height:1414px;
    background:var(--paper);box-shadow:0 10px 30px rgba(0,0,0,.35);overflow:hidden;
    font-family:"Rubik",sans-serif;color:var(--ink);
  }
  .scene-art{
    position:absolute;left:106px;top:250px;width:772px;height:764px;
    border-radius:48% 48% 40% 40% / 40% 40% 18% 18%;
    background:
      radial-gradient(circle at 58% 30%, #f07d22 0 34%, transparent 34.5%),
      linear-gradient(180deg,#f8f5e8 0%,#f8f5e8 28%,#3f6b5c 52%,#24443b 78%,#7a4a2a 100%);
  }
  .title{
    position:absolute;white-space:nowrap;
    font-family:"Yellowtail","Brush Script MT",cursive;color:var(--ink);line-height:1;
  }
  .title-main{top:50px;left:40px;width:920px;text-align:center;font-size:170px;letter-spacing:-1px}
  .title-sub{top:235px;left:560px;width:330px;font-size:104px;text-align:center}
  .referral{
    position:absolute;left:115px;top:940px;width:230px;height:88px;
    background:var(--orange);transform:rotate(-8deg);
    display:flex;align-items:center;justify-content:center;gap:8px;color:#fff;
  }
  .referral .pct{font-size:44px;font-weight:800}
  .referral .label{font-size:19px;font-weight:700;line-height:1}
  .location{
    position:absolute;left:149px;top:1050px;display:flex;align-items:center;gap:14px;white-space:nowrap;
  }
  .location .on{font-size:31px;font-weight:700;margin-top:14px}
  .location .lake{font-size:56px;font-weight:800;letter-spacing:1px;display:flex;align-items:center;gap:8px}
  .band{
    position:absolute;left:77px;top:1112px;width:824px;height:40px;background:var(--green);
    color:var(--cream);font-size:22px;font-weight:700;text-align:center;line-height:40px;letter-spacing:.3px;white-space:nowrap;
  }
  .brand-mark{
    position:absolute;left:60px;top:1200px;width:216px;text-align:center;
  }
  .brand-mark .name{font-size:25px;font-weight:800;color:var(--ink);display:flex;align-items:center;justify-content:center;gap:6px;white-space:nowrap}
  .brand-mark .dot{width:12px;height:12px;background:var(--ink);flex:none}
  .brand-mark .guide{margin-top:100px;font-family:"Roboto Condensed",sans-serif;font-size:13px;font-weight:700;line-height:1.05}
  .divider{position:absolute;left:292px;top:1188px;width:2px;height:182px;background:var(--ink)}
  .provide{position:absolute;left:326px;top:1190px}
  .provide h2{font-size:32px;font-weight:800;color:var(--green)}
  .amenities{list-style:none;display:grid;grid-template-columns:317px auto;grid-auto-flow:column;grid-template-rows:repeat(3,31px);margin-top:6px}
  .amenities li{font-size:24px;font-weight:500;display:flex;align-items:center;gap:8px;white-space:nowrap}
  .amenities svg{width:22px;height:22px;flex:none}
  .contact{
    position:absolute;left:326px;top:1338px;display:flex;align-items:center;gap:14px;white-space:nowrap;
    font-family:"Roboto Condensed",sans-serif;font-weight:700;font-size:31px;letter-spacing:.5px;
  }
  .contact .sep{width:2px;height:34px;background:var(--ink)}
  .contact .phone{color:var(--orange)}
</style>
</head>
<body>
  <main class="poster">
    <div class="scene-art" role="img" aria-label="Illustration of an orange sun and moon over pine forest and hills, with a retro cream and orange camper van, campfire and folding chair"></div>

    <h1 class="title title-main">Brightwater</h1>
    <p class="title title-sub">Resort</p>

    <div class="referral"><span class="pct">10%</span><span class="label">REFERRAL<br>DISCOUNT</span></div>

    <div class="location">
      <span class="on">LOCATED ON</span>
      <span class="lake">
        <svg width="28" height="40" viewBox="0 0 28 40" aria-hidden="true"><path d="M14 2C7 2 2 7.5 2 14c0 9 12 24 12 24s12-15 12-24C26 7.5 21 2 14 2z" fill="none" stroke="var(--orange)" stroke-width="4"/><circle cx="14" cy="14" r="4" fill="var(--orange)"/></svg>
        TUSKIN LAKE
      </span>
    </div>

    <div class="band">NORTHERN SASKATCHEWAN LARGER SEASONAL SITES &amp; LIMITED SITES</div>

    <div class="brand-mark">
      <div class="name"><span class="dot"></span>BRIGHTWATER</div>
      <div class="guide">Brand Guide<br>NOVEMBER 2021</div>
    </div>

    <div class="divider"></div>

    <section class="provide">
      <h2>WE PROVIDE</h2>
      <ul class="amenities">
        <li><svg viewBox="0 0 22 22"><path d="M3 12l5 6L19 3" fill="none" stroke="var(--orange)" stroke-width="3.5" stroke-linecap="round"/></svg>Marina &amp; lake access</li>
        <li><svg viewBox="0 0 22 22"><path d="M3 12l5 6L19 3" fill="none" stroke="var(--orange)" stroke-width="3.5" stroke-linecap="round"/></svg>Sauna or plunge</li>
        <li><svg viewBox="0 0 22 22"><path d="M3 12l5 6L19 3" fill="none" stroke="var(--orange)" stroke-width="3.5" stroke-linecap="round"/></svg>Disc golf</li>
        <li><svg viewBox="0 0 22 22"><path d="M3 12l5 6L19 3" fill="none" stroke="var(--orange)" stroke-width="3.5" stroke-linecap="round"/></svg>Hiking or quad trails</li>
        <li><svg viewBox="0 0 22 22"><path d="M3 12l5 6L19 3" fill="none" stroke="var(--orange)" stroke-width="3.5" stroke-linecap="round"/></svg>Pet friendly.</li>
      </ul>
    </section>

    <div class="contact">
      <span class="web">brightwaterresort.ca</span>
      <span class="sep"></span>
      <span class="phone">1-306-555-0148</span>
    </div>
  </main>
</body>
</html>
```